Kestrow-Holdings. Limestone; improving the world

New Limestone company and need logo design.
Limestone offsets carbon mitigation industries restore and replenish soil fertilities in the Prairies, the breadbasket of the world. At the same time, Limestone is proving a critical emergent component of carbon capture sequestration technology will therefore play a critical role in the development of the western Canadian energy industries
Our limestone resources are situated in the foothills of the Canadian Rockies well-positioned above the sprawling fields of the vast peace district.
Target Market(s)
Agriculture and oli sites
Logo Text
Kestrow Holdings
Number of Pages Required
3 page

```html
<!DOCTYPE html>
<html lang="en">
<head>
<meta charset="utf-8">
<title>Kestrow Holdings</title>
<link rel="stylesheet" href="https://fonts.googleapis.com/css2?family=Lato:ital,wght@0,400;0,700;0,900;1,400&family=Oswald:wght@400&display=swap">
<style>
:root{
  --green:#2a8a15;
  --blue:#1a5fc4;
  --brown:#553c22;
  --ink:#333333;
  --text:#444444;
  --light:#f4f4f4;
  --white:#ffffff;
}
*{margin:0;padding:0;box-sizing:border-box}
html,body{width:1200px;height:3013px;overflow:hidden}
body{position:relative;background:var(--white);font-family:'Lato',sans-serif;color:var(--text)}
.abs{position:absolute}

/* header */
.site-header{left:0;top:0;width:1200px;height:97px;background:var(--white)}
.brand{left:75px;top:24px;font-family:'Oswald',sans-serif;font-size:38px;color:var(--green);letter-spacing:.5px;line-height:50px}
.main-nav{right:74px;top:42px;display:flex;gap:31px;font-size:13px;font-weight:700;color:#222}
.main-nav .active{color:var(--blue)}

/* hero */
.hero{left:0;top:97px;width:1200px;height:666px;background:linear-gradient(180deg,#8e7448 0%,#6b6a4c 22%,#7d7d6c 45%,#8f8d83 70%,#6d6a60 100%)}
.hero-title{left:0;top:318px;width:1200px;text-align:center;font-size:68px;font-weight:900;color:var(--white);line-height:80px}
.hero-sub{left:250px;top:397px;width:700px;text-align:center;font-size:22px;line-height:34px;color:var(--white)}
.btn-solid{left:518px;top:482px;width:165px;height:45px;background:var(--green);color:var(--white);font-size:14px;font-weight:700;display:flex;align-items:center;justify-content:center}
.dots{left:74px;top:708px;display:flex;gap:10px}
.dots span{width:11px;height:11px;border-radius:50%;background:var(--white)}
.dots span:first-child{background:var(--blue)}

/* news card */
.news-card{left:794px;top:708px;width:332px;height:383px;background:var(--white);box-shadow:0 2px 10px rgba(0,0,0,.12);padding:20px 22px}
.news-card h3{font-size:24px;font-weight:700;color:var(--ink);margin-bottom:18px}
.news-item{display:flex;gap:15px;margin-bottom:26px}
.news-thumb{width:71px;height:71px;flex:none;margin-top:2px}
.news-item h4{font-size:14px;font-weight:700;color:var(--blue);margin-bottom:3px}
.news-item p{font-size:13px;line-height:20px;color:var(--text)}

/* welcome */
.section-title{font-size:38px;font-weight:700;color:var(--ink);line-height:46px}
.rule{height:3px;width:89px;background:var(--green)}
.welcome-title{left:80px;top:804px}
.welcome-rule{left:75px;top:863px}
.welcome-text{left:75px;top:891px;width:690px;font-size:17px;line-height:27.6px}
.btn-outline{height:45px;width:165px;border:1.5px solid var(--green);color:var(--green);font-size:14px;font-weight:700;display:flex;align-items:center;justify-content:center}
.welcome-btn{left:75px;top:1047px}

/* mission */
.mission{left:0;top:1158px;width:1200px;height:375px;background:linear-gradient(100deg,#1b57c2 0%,#1d6a6a 45%,#268514 100%)}
.mission-title{left:0;top:1231px;width:1200px;text-align:center;color:var(--white);font-size:38px;font-weight:700;line-height:46px}
.mission-rule{left:556px;top:1290px;background:var(--white)}
.mission-text{left:110px;top:1317px;width:980px;text-align:center;color:var(--white);font-style:italic;font-size:19.5px;line-height:33px}

/* services */
.services{left:0;top:1533px;width:1200px;height:460px;background:var(--light)}
.center-title{left:0;width:1200px;text-align:center}
.services-title{top:1589px}
.services-rule{left:556px;top:1648px}
.service-feature{left:75px;top:1687px;width:346px;height:227px;background:var(--brown);color:var(--white);text-align:center;padding:44px 30px 0}
.service-feature h3{font-size:23px;font-weight:700;margin-bottom:14px}
.service-feature p{font-size:14.5px;line-height:22px}
.service{top:1687px;width:346px;height:227px;text-align:center}
.service-icon{width:100px;height:86px;margin:40px auto 22px;border-radius:8px;background:#cdbfae}
.service h3{font-size:23px;font-weight:700;color:var(--brown)}
.service-divider{left:778px;top:1687px;width:1px;height:227px;background:#c9c9c9}

/* sustainability */
.sustain-photo{left:0;top:1993px;width:601px;height:416px;background:linear-gradient(180deg,#3c78c6 0%,#8da3b8 32%,#3d5a3a 58%,#1f8a9a 78%,#2e5a2a 100%)}
.sustain-panel{left:601px;top:1993px;width:599px;height:416px;background:var(--light)}
.sustain-title{left:655px;top:2033px}
.sustain-rule{left:650px;top:2091px}
.sustain-text{left:650px;top:2120px;width:486px;font-size:17px;line-height:27.6px}
.sustain-btn{left:650px;top:2316px}

/* partners */
.partners-title{top:2461px}
.partners-rule{left:556px;top:2523px}
.partner{top:2563px;width:241px;height:96px;background:var(--white);box-shadow:0 2px 8px rgba(0,0,0,.12);display:flex;align-items:center;justify-content:center;gap:10px;font-size:30px;font-weight:700;color:#2b2b2b}
.partner.selected{border:2px solid var(--blue)}
.partner i{width:36px;height:36px;border-radius:50%;display:block}

/* footer */
.site-footer{left:0;top:2743px;width:1200px;height:270px;background:var(--brown);color:var(--white)}
.footer-brand{left:75px;top:2806px;font-family:'Oswald',sans-serif;font-size:30px;line-height:40px}
.footer-copy{left:75px;top:2855px;font-size:13px;line-height:24px}
.social{left:75px;top:2915px;display:flex;gap:19px}
.social span{width:20px;height:20px;border-radius:50%;background:var(--white)}
.footer-col h4{font-size:16px;font-weight:700;margin-bottom:6px}
.sitemap{left:386px;top:2800px}
.sitemap a{display:block;color:var(--white);text-decoration:none;font-size:13px;line-height:23.7px}
.subscribe{left:568px;top:2800px}
.email-input{left:568px;top:2839px;width:243px;height:36px;background:var(--white);color:#333;font-size:14px;padding:0 13px;display:flex;align-items:center}
.signup{left:720px;top:2885px;width:91px;height:37px;background:var(--green);font-size:14px;font-weight:700;display:flex;align-items:center;justify-content:center}
.contact{left:888px;top:2800px}
.contact-line{display:flex;gap:18px;font-size:14px;line-height:21px;margin-bottom:10px;width:260px}
.contact-line svg{flex:none;margin-top:3px}
</style>
</head>
<body>

<header class="abs site-header">
  <div class="abs brand">KESTROW HOLDINGS</div>
  <nav class="abs main-nav">
    <span class="active">HOME</span><span>ABOUT US</span><span>SERVICES</span><span>RESOURCES</span><span>LATEST NEWS</span><span>CONTACT</span>
  </nav>
</header>

<section class="abs hero" role="img" aria-label="Rocky limestone pavement landscape under an evening sky"></section>
<h1 class="abs hero-title">KESTROW HOLDINGS</h1>
<p class="abs hero-sub">Sed ut perspiciatis unde omnis iste natus error sit voluptatem accusantium doloremque laudantium.</p>
<div class="abs btn-solid">READ MORE</div>
<div class="abs dots"><span></span><span></span><span></span><span></span></div>

<aside class="abs news-card">
  <h3>Latest News</h3>
  <div class="news-item">
    <div class="news-thumb" role="img" aria-label="Limestone field at sunset" style="background:linear-gradient(#b68a5a,#6a6a60)"></div>
    <div><h4>Lorem ipsumdolor...</h4><p>Consectetur adipisicing elit, sed do eiusmod tempor incididunt ut labore et...</p></div>
  </div>
  <div class="news-item">
    <div class="news-thumb" role="img" aria-label="Pile of white limestone rocks" style="background:linear-gradient(#d8d8d4,#7d7a72)"></div>
    <div><h4>Lorem ipsumdolor...</h4><p>Consectetur adipisicing elit, sed do eiusmod tempor incididunt ut labore et...</p></div>
  </div>
  <div class="news-item">
    <div class="news-thumb" role="img" aria-label="Lone tree on limestone at dusk" style="background:linear-gradient(#c88a6a,#5a4a58)"></div>
    <div><h4>Lorem ipsumdolor...</h4><p>Consectetur adipisicing elit, sed do eiusmod tempor incididunt ut labore et...</p></div>
  </div>
</aside>

<h2 class="abs section-title welcome-title">Welcome to Our Website</h2>
<div class="abs rule welcome-rule"></div>
<p class="abs welcome-text">Lorem ipsum dolor sit amet, consectetur adipisicing elit, sed do eiusmod tempor incididunt ut labore et doloreasdes magna aliqua. Ut enim ad minim veniam, quis nostrud exercitation ullamco laboris nisi ut aliquip ex ea commodalo consequat. Duis aute irure dolor in reprehenderit in voluptate velit esse cillum dolore eu fugiat nulla pariatur.</p>
<div class="abs btn-outline welcome-btn">READ MORE</div>

<section class="abs mission"></section>
<h2 class="abs mission-title">Our Mission</h2>
<div class="abs rule mission-rule"></div>
<p class="abs mission-text">“ Lorem ipsum dolor sit amet, consectetur adipisicing elit, sed do eiusmod tempor incididunt ut labore et doloreasdes magna aliqua. Ut enim ad minim veniam, quis nostrud exercitation ullamco laboris nisi ut aliquip ex ea commodalo consequat. Duis aute irure dolor in&nbsp; reprehenderit in voluptate velit esse cillum dolore<br>eu fugiat nulla pariatur...”</p>

<section class="abs services"></section>
<h2 class="abs section-title center-title services-title">Our Services</h2>
<div class="abs rule services-rule"></div>
<div class="abs service-feature">
  <h3>Neque Porro Quisquam</h3>
  <p>Lorem ipsum dolor sit amet, consectetur adipisicing elit, sed do eiusmod tempor incididunt ut labore et doloreasdes magna aliqua..</p>
</div>
<div class="abs service" style="left:427px">
  <div class="service-icon" role="img" aria-label="Limestone rock icon"></div>
  <h3>Neque Porro Quisquam</h3>
</div>
<div class="abs service-divider"></div>
<div class="abs service" style="left:779px">
  <div class="service-icon" role="img" aria-label="Renewal cycle icon with leaves"></div>
  <h3>Neque Porro Quisquam</h3>
</div>

<div class="abs sustain-photo" role="img" aria-label="Mountain lake with snowy peaks and pine forest"></div>
<section class="abs sustain-panel"></section>
<h2 class="abs section-title sustain-title">Sustainability</h2>
<div class="abs rule sustain-rule"></div>
<p class="abs sustain-text">Lorem ipsum dolor sit amet, consectetur adipisicing elit, sed do eiusmod tempor incididunt ut labore et doloreasdes magna aliqua. Ut enim ad minim veniam, quis nostrud exercitation ullamco laboris nisi ut aliquip ex ea commodalo consequat. Duis aute irure dolor in&nbsp; reprehenderit in voluptate velit esse cillum dolore eu fugiat nulla pariatur.</p>
<div class="abs btn-outline sustain-btn">READ MORE</div>

<h2 class="abs section-title center-title partners-title">Partnerships</h2>
<div class="abs rule partners-rule"></div>
<div class="abs partner selected" style="left:75px"><i style="background:#e85a1c"></i>Brightwell</div>
<div class="abs partner" style="left:345px"><i style="background:#ef6a1a"></i>Northmark</div>
<div class="abs partner" style="left:615px"><i style="background:#f2a41c"></i>Fieldstone</div>
<div class="abs partner" style="left:885px"><i style="background:#2a6fd8"></i>Corvane</div>

<footer class="abs site-footer"></footer>
<div class="abs footer-brand" style="color:var(--white)">KESTROW HOLDINGS</div>
<p class="abs footer-copy" style="color:var(--white)">Copyright © 2021 Kestrow Holdings<br>All Right Reserved</p>
<div class="abs social" aria-label="Social links"><span></span><span></span><span></span><span></span><span></span></div>

<div class="abs footer-col sitemap" style="color:var(--white)">
  <h4>SITE MAP</h4>
  <a>Home</a><a>About Us</a><a>Services</a><a>Resources</a><a>Latest News</a><a>Contact</a>
</div>
<div class="abs footer-col subscribe" style="color:var(--white)"><h4>EMAIL SUBSCRIBE</h4></div>
<div class="abs email-input">Enter Emial Address</div>
<div class="abs signup" style="color:var(--white)">SIGN UP</div>

<div class="abs footer-col contact" style="color:var(--white)">
  <h4 style="margin-bottom:14px">CONTATC US</h4>
  <div class="contact-line">
    <svg width="12" height="14" viewBox="0 0 12 14"><path d="M6 0a5 5 0 0 0-5 5c0 3.5 5 9 5 9s5-5.5 5-9a5 5 0 0 0-5-5zm0 7a2 2 0 1 1 0-4 2 2 0 0 1 0 4z" fill="#fff"/></svg>
    <span>14 Ridgeway Court, Calder Falls, 40210</span>
  </div>
  <div class="contact-line">
    <svg width="12" height="12" viewBox="0 0 12 12"><path d="M2.5 0l2 2.8-1.2 1.4c.8 1.8 2.1 3.1 3.9 3.9l1.4-1.2L11.4 9 10 11.5C5 11 1 7 .5 2z" fill="#fff"/></svg>
    <span>1-800-555-0148</span>
  </div>
  <div class="contact-line">
    <svg width="13" height="10" viewBox="0 0 13 10"><rect width="13" height="10" rx="1" fill="#fff"/><path d="M0 1l6.5 5L13 1" stroke="#553c22" stroke-width="1.3" fill="none"/></svg>
    <span>hello@kestrowholdings.example</span>
  </div>
</div>

</body>
</html>
```